“Bright Tide” Spring Fair Poster

We are putting together a school and community fair. We need a poster designed to advertise the event and give some important information to would be attendees. We’d like the poster graphics to evoke a minimalistic and futuristic aesthetic, be bold, yet fun! We will printing the posters, so we will need for them to be at high resolution and ready to send to print.

Target Market(s)

Students, Parents, and Community members

Industry/Entity Type

School

Font styles to use
Sans Serif

Colors
33a6d7
fabb78
9d9d9d
ffffff
1b1b1b
33b8a4

Requirements
Must have
• Bright Tide
• Birch & Lantern Spring Fair 2018
• Friday, May 18th
• 5:00-9:00pm
• Tickets Will Be Available at Select Pick up & Drop Off Times
• Come Enjoy a Futuristic Evening of Food, Music, Entertainment, & Fun!
Nice to have
• We’d love to see a bold and graphic poster with a futuristic feel!
• See the sample image below from previous event poster and additional images for mood and inspiration. Would love to see metallics (silver or metallic colors)

```html
<!DOCTYPE html>
<html lang="en">
<head>
<meta charset="utf-8">
<title>Bright Tide — Birch &amp; Lantern Spring Fair 2018</title>
<link rel="stylesheet" href="https://fonts.googleapis.com/css2?family=Anton&family=Jost:ital,wght@0,400;0,700;1,300;1,400&family=Pathway+Gothic+One&display=swap">
<style>
  :root {
    --ink: #161719;
    --paper: #ffffff;
    --mint: #4cf08c;
    --mint-soft: #d8fbe6;
    --sky: #54d0ec;
    --peach: #f5b172;
  }
  * { margin: 0; padding: 0; box-sizing: border-box; }
  html, body { width: 776px; height: 1200px; overflow: hidden; background: var(--ink); }
  .poster { position: relative; width: 776px; height: 1200px; background: var(--ink); overflow: hidden; }
  .poster > * { position: absolute; }

  .top-band { left: 0; top: 37px; width: 776px; height: 41px; background: var(--mint); }

  .frame-square { left: 166px; top: 286px; width: 450px; height: 450px; background: var(--paper); }
  .frame-texture {
    left: 176px; top: 296px; width: 430px; height: 430px;
    background: radial-gradient(ellipse at 55% 45%, var(--mint-soft) 0%, var(--paper) 75%);
  }

  .peach-tab { height: 22px; background: var(--peach); }
  .tab-left-top { left: 99px; top: 330px; width: 67px; }
  .tab-right-top { left: 616px; top: 330px; width: 90px; }
  .tab-left-low { left: 99px; top: 677px; width: 67px; }
  .tab-right-low { left: 616px; top: 677px; width: 90px; }

  .sky-bar { background: var(--sky); }
  .bar-one { left: 209px; top: 194px; width: 25px; height: 293px; }
  .bar-two { left: 265px; top: 194px; width: 27px; height: 482px; }
  .bar-three { left: 494px; top: 355px; width: 26px; height: 483px; }
  .bar-four { left: 552px; top: 544px; width: 26px; height: 294px; }

  .year-band { top: 557px; height: 55px; background: var(--peach); }
  .year-band-left { left: 0; width: 302px; }
  .year-band-right { left: 481px; width: 295px; }

  .event-name {
    left: 166px; top: 146px;
    font-family: "Jost", sans-serif; font-style: italic; font-weight: 400;
    font-size: 68px; line-height: 60px; letter-spacing: -1px;
    color: var(--paper); text-transform: uppercase;
  }

  .headline, .guides { left: 0; top: 0; width: 776px; height: 1200px; }

  .info-bar { height: 41px; background: var(--mint); display: flex; align-items: center; color: var(--paper); }
  .info-date, .info-time { left: 0; width: 520px; padding-left: 297px; font-family: "Jost", sans-serif; font-size: 22px; letter-spacing: 0.5px; }
  .info-date { top: 909px; }
  .info-time { top: 1032px; }
  .info-tickets, .info-invite { left: 271px; width: 505px; padding-left: 25px; font-family: "Pathway Gothic One", sans-serif; font-size: 19px; }
  .info-tickets { top: 970px; }
  .info-invite { top: 1093px; }
</style>
</head>
<body>
<main class="poster">
  <div class="top-band"></div>

  <div class="frame-square"></div>
  <div class="frame-texture" role="img" aria-label="Soft mint diamond texture filling the central square"></div>

  <div class="peach-tab tab-left-top"></div>
  <div class="peach-tab tab-right-top"></div>
  <div class="peach-tab tab-left-low"></div>
  <div class="peach-tab tab-right-low"></div>

  <div class="sky-bar bar-one"></div>
  <div class="sky-bar bar-two"></div>
  <div class="sky-bar bar-three"></div>
  <div class="sky-bar bar-four"></div>

  <div class="year-band year-band-left"></div>
  <div class="year-band year-band-right"></div>

  <h1 class="event-name">Bright<br>Tide</h1>

  <svg class="headline" viewBox="0 0 776 1200" aria-label="Birch &amp; Lantern Spring Fair 2018">
    <text x="393" y="373" text-anchor="middle" fill="var(--peach)" font-family="Jost, sans-serif" font-style="italic" font-weight="300" font-size="22">BIRCH &amp; LANTERN</text>
    <text x="274" y="443" textLength="236" lengthAdjust="spacingAndGlyphs" fill="var(--ink)" font-family="Anton, sans-serif" font-size="78">SPRING</text>
    <text x="274" y="545" textLength="236" lengthAdjust="spacingAndGlyphs" fill="var(--ink)" font-family="Anton, sans-serif" font-size="126">FAIR</text>
    <text x="311" y="610" textLength="162" lengthAdjust="spacingAndGlyphs" fill="var(--peach)" font-family="Jost, sans-serif" font-weight="700" font-size="74">2018</text>
  </svg>

  <div class="info-bar info-date">FRIDAY, MAY 18TH</div>
  <div class="info-bar info-tickets">Tickets Will Be Available at Select Pick up &amp; Drop Off Times</div>
  <div class="info-bar info-time">5:00PM - 9:00PM</div>
  <div class="info-bar info-invite">Come Enjoy a Futuristic Evening of Food, Music, Entertainment, &amp; Fun!</div>

  <svg class="guides" viewBox="0 0 776 1200" aria-hidden="true">
    <g stroke="var(--paper)" stroke-width="3" stroke-dasharray="14 10" fill="none">
      <line x1="64" y1="0" x2="64" y2="1200"/>
      <line x1="430" y1="180" x2="776" y2="180"/>
      <line x1="674" y1="349" x2="674" y2="1200"/>
    </g>
  </svg>
</main>
</body>
</html>
```